Business cards, envelopes, etc. for real estate company

We have a finished logo for our real estate company. We need a corporate identity package with the following items:

1. Business Cards
2. Letterhead/Stationary - with 2 pages:
-1st page with full header
-2nd page without top header
3. Concise and professional e-mail signature image
4. Fax coversheet
5. Shipping label, with our return address and a mail-to address (on one label)

We need these to be editable. We don't know the industry standard for these items but perhaps you can provide them to us in .PDF and Word format (and if you use Adobe Illustrator for them, .AI as well).

Please use the attached placeholder logo in your design entry. We will provide you with the original logo to swap in (same size and design, just different text) when we choose your entry.

Please include the following information on the letterhead and business cards:

58 West 41st Street
3rd Floor West
New York, NY 10047

Tel: 212-555-0148
Fax :212-555-0148

Please contact us if you have any questions about this contest.
Updates

Hi,

Thanks for your interest in this project. The logo to use should be working now. Please contact me if you have any further issues or questions.

I look forward to seeing your submissions. 

Hi,

We first wish to thank you all for your submissions. 

Here is some general feedback regarding the designs shown:

1. We would prefer square (as opposed to rounded) business cards.

2. For the fax coversheets, we are looking with a designed look. While we understand these are samples, we don't want it to appear as if it a standard block of text or a fax template from a word processing program.

3. For the 1st page of letterhead and envelopes, we do need an office address on them. The envelopes should have space for a stamp in the top right corner. We would prefer the envelopes not to have colored stripes.

4. We think a watermark of the logo is an interesting idea on the business cards and/or letterhead. This may be something to try. However, it is not strictly necessary and we would like to evaluate designs with and without it.

In general we are looking for a clean yet professional look.

We are actively reviewing all entries and thank you for your time and creativity.

One last comment: We understand making all objects in the brief takes some time. However, we want to remind all the designers that this contest is for more than just business cards (envelopes, letterheads, etc.) so if we choose your design, those items will be expected. Please refer to the original brief to see what we are requesting.

If you provide a mockup of any item listed in the brief (in addition to business cards) it would help us visualize your entire vision for this project.

Industry/Entity Type

Real Estate

```html
<!DOCTYPE html>
<html lang="en">
<head>
<meta charset="utf-8">
<title>Harlow &amp; Harlow — Business Card</title>
<link href="https://fonts.googleapis.com/css2?family=Arimo:wght@400;700&display=swap" rel="stylesheet">
<style>
  :root {
    --navy: #1d3a5c;
    --ink: #2b2b2b;
    --card: #f4f4f4;
    --backdrop: #e6e7e8;
    --rule: #4a5a70;
  }
  * { box-sizing: border-box; margin: 0; padding: 0; }
  html, body {
    width: 1200px; height: 800px; overflow: hidden;
    background: var(--backdrop);
    font-family: "Arimo", Arial, sans-serif;
  }
  .stage { position: relative; width: 1200px; height: 800px; }
  .card {
    position: absolute; width: 504px; height: 288px;
    background: var(--card);
    box-shadow: 0 2px 10px rgba(0,0,0,0.12);
  }
  .card--front { left: 66px; top: 256px; }
  .card--back { left: 630px; top: 256px; display: flex; align-items: center; justify-content: center; }

  .brand { position: absolute; left: 40px; top: 46px; display: flex; align-items: center; gap: 10px; }
  .brand__dot { width: 10px; height: 10px; border-radius: 50%; background: var(--navy); }
  .brand__name { font-size: 20px; line-height: 1; color: var(--navy); font-weight: 400; white-space: nowrap; }

  .contact { position: absolute; right: 40px; top: 40px; display: flex; flex-direction: column; gap: 4px; list-style: none; }
  .contact__row { display: flex; align-items: center; justify-content: flex-end; gap: 8px; font-size: 12px; color: var(--ink); }
  .icon { width: 13px; height: 13px; background: var(--navy); display: inline-block; flex: none; }
  .icon svg { display: block; width: 13px; height: 13px; }

  .divider { position: absolute; left: 40px; right: 40px; top: 138px; height: 1px; background: var(--rule); }
  .edge-tick { position: absolute; left: 0; top: 150px; width: 4px; height: 12px; background: var(--navy); }

  .person { position: absolute; left: 40px; top: 156px; }
  .person__name { font-size: 16px; font-weight: 700; color: var(--navy); }
  .person__title { font-size: 10px; font-weight: 700; color: var(--navy); margin-top: 2px; }
  .address { margin-top: 12px; font-size: 12px; line-height: 1.35; color: var(--ink); font-style: normal; }

  .back-brand__name { font-size: 28px; line-height: 1; color: var(--navy); font-weight: 400; white-space: nowrap; }
</style>
</head>
<body>
<main class="stage">
  <section class="card card--front" aria-label="Business card front">
    <div class="brand">
      <span class="brand__dot"></span>
      <span class="brand__name">Harlow &amp; Harlow</span>
    </div>

    <ul class="contact">
      <li class="contact__row">212-555-0148
        <span class="icon"><svg viewBox="0 0 13 13"><path d="M4 3 L5.5 3 L6 5 L5 5.8 Q6 7.5 7.2 8 L8 7 L10 7.5 L10 9 Q6 9.5 4 5 Z" fill="#fff"/></svg></span>
      </li>
      <li class="contact__row">212-555-0148
        <span class="icon"><svg viewBox="0 0 13 13"><rect x="3" y="5" width="7" height="5" fill="#fff"/><rect x="4" y="3" width="5" height="2" fill="#fff"/></svg></span>
      </li>
      <li class="contact__row">info@harlowhomes.com
        <span class="icon"><svg viewBox="0 0 13 13"><rect x="3" y="4" width="7" height="5" fill="none" stroke="#fff"/><path d="M3 4 L6.5 7 L10 4" fill="none" stroke="#fff"/></svg></span>
      </li>
      <li class="contact__row">www.harlowhomes.com
        <span class="icon"><svg viewBox="0 0 13 13"><circle cx="6.5" cy="6.5" r="3.5" fill="none" stroke="#fff"/><path d="M3 6.5 H10 M6.5 3 V10" stroke="#fff" stroke-width="0.8"/></svg></span>
      </li>
    </ul>

    <div class="divider"></div>
    <div class="edge-tick"></div>

    <div class="person">
      <p class="person__name">Daniel Whitford</p>
      <p class="person__title">Founder</p>
      <address class="address">
        58 West 41st Street<br>
        3rd Floor West<br>
        New York, NY 10047
      </address>
    </div>
  </section>

  <section class="card card--back" aria-label="Business card back">
    <span class="back-brand__name">Harlow &amp; Harlow</span>
  </section>
</main>
</body>
</html>
```